Corporate Design für Zaubertheater
Zielgruppe
Wir planen ein Zaubertheater und suchen dafür ein Logo und eine CI mit Empfehlungen für Farbklima, Layout und Schriftart, exemplarisch ausgeführt als Briefpapier, Visitenkarte und einer Internet-Startseite.
Das Logo kann komplett unabhängig vom Schriftzug stehen oder mit dem Wort „Mondkranich“ verbunden sein.
Wenn Logo und Text eine Einheit bilden, dann wäre es gut, wenn man wechselnde „Untertitel“ mit einbauen könnte:
• Mondkranich – Zaubertheater
• Mondkranich – Musik im Foyer
• Mondkranich – Theater Ober-Ingelheim
Worum geht´s?
• Es geht um ein kleines Theater
• mit phantasievoll-nostalgischem Ambiente (historische Einflüsse von der Viktorianik bis zu den 20er Jahren und phantastische Einflüsse aus dem Steampunk)
• in dem in familiärer Atmosphäre (persönliche Begrüßung durch den Künstler, gemeinsamer Willkommens-Sekt vor der Show, Ambiente zwischen Theater und Salon/Wohnzimmer)
• Zauberkunst für Erwachsene gezeigt wird.
• Dazu wird in der Regel vor der Show und in der Pause ein kaltes Buffet angeboten.
Aufgabenstellung
Was wir NICHT wollen
• Anmutung von Kindertheater
• Zylinderhut, Kaninchen oder Zauberstab im Logo
Mögliche Motive wären z.B.
- Das Orangenbäumchen: https://bilderkammer-lutz.de/werke/4-alte-radierung-tafel-blauhof-kupfer.html
- Steampunkmotive/Zeitreisemotive: Uhren, Zeiger, Zahnräder, Kompassnadeln, Kompassrosetten
- Hände
- Ein Ring in einer Nuss in einem Ei in einer Orange
- DAS IST JEDOCH KEINE VORGABE!! nur mögliche Inspiration.

```html
<!DOCTYPE html>
<html lang="de">
<head>
<meta charset="utf-8">
<title>Mondkranich Zaubertheater – Briefpapier</title>
<link href="https://fonts.googleapis.com/css2?family=Jost:wght@300;400;500;600&display=swap" rel="stylesheet">
<style>
  :root{
    --night:#2b3547;
    --night-deep:#1c2330;
    --night-light:#3a465b;
    --gold:#b8945c;
    --gold-seal:#b08b55;
    --ink:#4a4a4a;
    --ink-dark:#3a3a3a;
    --mist:#f1f0ec;
    --paper:#ffffff;
  }
  *{margin:0;padding:0;box-sizing:border-box}
  html,body{width:848px;height:1200px;overflow:hidden;background:var(--paper)}
  .letter{position:relative;width:848px;height:1200px;font-family:'Jost',sans-serif;color:var(--ink)}

  .masthead{position:absolute;left:0;top:0;width:848px;height:192px;
    background:radial-gradient(ellipse at 50% 40%,var(--night-light) 0%,var(--night) 55%,var(--night-deep) 100%)}
  .brand{position:absolute;left:0;right:0;top:96px;text-align:center;color:var(--gold);font-weight:500}
  .brand-name{font-size:36px;letter-spacing:2px;line-height:1}
  .brand-sub{font-size:13.5px;letter-spacing:4px;margin-top:22px;line-height:1}

  .backdrop{position:absolute;left:0;top:800px;width:848px;height:400px;
    background:radial-gradient(ellipse at 45% 75%,var(--mist) 0%,rgba(241,240,236,.6) 45%,rgba(255,255,255,0) 75%)}

  .sender{position:absolute;right:48px;top:208px;text-align:right;font-style:normal;font-size:13px;font-weight:400;line-height:20px;letter-spacing:.7px;color:var(--ink-dark)}
  .sender-name{font-weight:500}
  .sender-web{font-weight:600}

  .recipient{position:absolute;left:101px;top:263px;font-style:normal;font-size:11px;line-height:20px;letter-spacing:2.3px;color:var(--ink-dark)}

  .date{position:absolute;right:48px;top:368px;font-size:12.5px;letter-spacing:.8px;color:var(--ink-dark)}

  .subject{position:absolute;left:285px;top:376px;font-size:17px;font-weight:500;line-height:28px;letter-spacing:2px;color:var(--ink-dark)}

  .body{position:absolute;left:285px;top:472px;font-size:14px;font-weight:300;line-height:25.7px;letter-spacing:1.55px;color:var(--ink)}
  .body p{margin-bottom:25.7px}
  .body .line{display:block;white-space:nowrap}

  .bank{position:absolute;left:49px;top:1044px;font-size:9.5px;line-height:12px;letter-spacing:2px;color:var(--ink-dark)}
  .bank p+p{margin-top:12px}

  .seal{position:absolute;left:611px;top:962px;width:172px;height:172px}
</style>
</head>
<body>
<main class="letter">
  <header class="masthead" role="img" aria-label="Dunkelblaues Kopfbild mit alten Astrolabien und Messinstrumenten">
    <div class="brand">
      <div class="brand-name">MONDKRANICH</div>
      <div class="brand-sub">ZAUBERTHEATER</div>
    </div>
  </header>

  <div class="backdrop" role="img" aria-label="Zarte helle Zahnräder und Flügel als Hintergrundmotiv"></div>

  <address class="sender">
    <div class="sender-name">MONDKRANICH Zaubertheater</div>
    <div>Uhrmachergasse 5</div>
    <div>48527 Musterstadt</div>
    <div>Tel.: 0251 / 738 916</div>
    <div>info@mondkranich.de</div>
    <div class="sender-web">www.mondkranich.de</div>
  </address>

  <address class="recipient">
    <div>Frau Lena Hartwig</div>
    <div>Lindenhofweg 7</div>
    <div>45279 Musterstadt</div>
  </address>

  <div class="date">Datum 20.08.2020</div>

  <h1 class="subject">Wir laden dich zu unserem neuen<br>Eventlaunch ein am 28.12.2020</h1>

  <section class="body">
    <p>
      <span class="line">Liebe Lena,</span>
      <span class="line">Et omnist, consequ idendem aceatemquiae poreperum dem quamus</span>
      <span class="line">neceaquas quatatum quam, ut lacerciet qui beaquis ipsae et volupta</span>
      <span class="line">tquiati quam sape nus velent que quam, cumque cone sitam repudi-</span>
      <span class="line">ae. Ut quam aspereserum corroribus, optur?</span>
    </p>
    <p>
      <span class="line">Elitas etusae istia sam as alit, si dolut as simet laut eic totati qui</span>
      <span class="line">simolor ibusaperum ipidis ut abore delenti istotat quibeatem eos</span>
      <span class="line">eatem quia num as veriaec temolor rovitia inctia volorum fuga. Nem</span>
      <span class="line">dolo dolum reped que rendund amendis volores sentiur?</span>
      <span class="line">Ducit versperum nonsentio. Nam que alitas non cusant facerrum fugit</span>
      <span class="line">et, unt rerionsequas qui bererumqui to ipis ad qui derspide pa aut et</span>
      <span class="line">od quunt.</span>
    </p>
    <p>
      <span class="line">Giam endipsa veliquis a dit, imusciate latest, vit ate earum solorit</span>
      <span class="line">optiiscim quae parit ipsant ut ut eosamen imporepe liti nonsequi si</span>
      <span class="line">dolupta epudaecto etur, omnim exceped modit atur? Os im ratquis</span>
      <span class="line">sequatiunto tecti alitatis consequatur.</span>
    </p>
    <p><span class="line">Mit magischen Grüßen,</span></p>
  </section>

  <footer class="bank">
    <p>Spar- und Darlehnskasse<br>Muster Bank eG<br>KTO: 471902386s<br>BLZ: 5172093</p>
    <p>KTO Inh.: MONDKRANICH GmbH<br>IBAN: DE12 3456 7890 1234 5678 90<br>BIC: MUSTDEX1XXX<br>Steuer ID: 12 345 678 901</p>
  </footer>

  <svg class="seal" viewBox="0 0 172 172" role="img" aria-label="Goldenes Siegel mit handgeschriebenem Schriftzug zur neuen Show ab Januar 2021">
    <circle cx="86" cy="86" r="83" fill="var(--gold-seal)"/>
    <circle cx="86" cy="86" r="84" fill="none" stroke="var(--gold-seal)" stroke-width="4" stroke-dasharray="2 2"/>
  </svg>
</main>
</body>
</html>
```